Commercial janitorial cleaning

Janitorial cleaning particularly for commercial buildings. Website needs to specify free estimates. Location of service is Hudson, Valatie, East Greenbush, Troy, Albany ny area. Services page with Janitorial services- General Office Cleaning, Construction Cleaning, Carpet Extraction, Consultation/Business, Lighting Maintenance, Seasonal Deep Cleaning, Window cleaning, Event Cleaning, Floor and Carpet Cleaning, Floor Striping and Waxing. Contact us page with email phone number on page and a request page that emails me if they have any questions. About us page-the picture of my family on it with a section I can type a story myself.

Target Market(s)

Commercial businesses

Industry/Entity Type

Janitorial Service

Number of Pages Required

4 page

Font styles to use
Serif
Sans Serif
Script

Colors
ec1f27
1b1b1b
ffffff
9d9d9d

Requirements
Must have
• Phone number 555-314-2760. Must have free estimates on home page. Going for industrial / modern look to website
Nice to have
• Logo is a red and black building so if those colors could be coordinated to website that would be awesome.

```html
<!DOCTYPE html>
<html lang="en">
<head>
<meta charset="utf-8">
<title>Northgate Cleaning Services</title>
<link href="https://fonts.googleapis.com/css2?family=Roboto:wght@300;400;500;700&display=swap" rel="stylesheet">
<style>
  :root {
    --brand-red: #ec1f27;
    --ink: #1b1b1b;
    --white: #ffffff;
    --grey: #9d9d9d;
    --bar-grey: #eeeef0;
    --band-grey: #f4f4f6;
    --muted: #6d6d6d;
  }
  * { box-sizing: border-box; margin: 0; padding: 0; }
  html, body {
    width: 1200px; height: 676px; overflow: hidden;
    background: var(--white);
    font-family: "Roboto", Arial, sans-serif;
    color: var(--ink);
  }
  .site { position: relative; width: 1200px; height: 676px; overflow: hidden; }
  .top-rule { height: 4px; background: var(--brand-red); }

  .header {
    height: 66px; display: flex; align-items: center;
    padding: 0 48px 0 44px; position: relative;
  }
  .brand { display: flex; align-items: center; gap: 8px; }
  .brand-mark { width: 38px; height: 38px; background: var(--brand-red); }
  .brand-name {
    color: var(--brand-red); font-weight: 700; font-size: 13px; line-height: 13px;
  }
  .main-nav {
    position: absolute; left: 50%; transform: translateX(-58%);
    display: flex; gap: 36px; font-size: 12.5px; color: var(--ink);
  }
  .cta-button {
    margin-left: auto; background: var(--brand-red); color: var(--white);
    font-weight: 700; font-size: 12px; padding: 7px 9px; border-radius: 4px;
  }

  .hero {
    position: relative; height: 430px;
    background: linear-gradient(100deg, #8f7f66 0%, #b1a48c 22%, #a29a8c 40%, #77736e 55%, #9c9c9c 72%, #d2d2d2 100%);
    display: flex; align-items: center; justify-content: center;
  }
  .hero-disc {
    width: 230px; height: 230px; border-radius: 50%;
    background: rgba(110, 108, 106, 0.55);
    display: flex; flex-direction: column; align-items: center; justify-content: center;
    color: var(--white); text-align: center; font-weight: 300;
    font-size: 27px; line-height: 34px; letter-spacing: 1px;
  }
  .hero-disc strong { font-weight: 700; font-size: 36px; line-height: 38px; letter-spacing: 0; }

  .info-bar {
    height: 36px; background: var(--bar-grey);
    display: flex; align-items: center; padding: 0 48px 0 80px;
    font-size: 13px; color: var(--muted); gap: 28px;
  }
  .info-item { display: flex; align-items: center; gap: 6px; }
  .info-item svg { fill: var(--muted); }
  .social { margin-left: auto; display: flex; align-items: center; gap: 14px; }
  .social-dot { width: 17px; height: 17px; border-radius: 3px; }
  .social-dot.blue { background: #3b5998; }
  .social-dot.red { background: #dd4b39; }
  .social-dot.sky { background: #1da1f2; border-radius: 50%; }

  .welcome { text-align: center; padding-top: 18px; }
  .welcome h1 { font-size: 21px; font-weight: 500; }
  .welcome h1 span { color: var(--brand-red); }
  .dotted-rule {
    margin: 12px 50px 0 60px; border-top: 1px dashed var(--brand-red);
  }
  .welcome p {
    margin: 14px 50px 0; font-size: 12px; line-height: 19px; color: var(--ink);
  }
  .lower-band {
    position: absolute; left: 0; right: 0; top: 652px; bottom: 0;
    background: var(--band-grey);
  }
  .outline-button {
    position: absolute; left: 50%; top: 10px; transform: translateX(-50%);
    width: 180px; height: 30px; border: 1px solid var(--brand-red); border-radius: 4px;
    background: var(--white);
  }
</style>
</head>
<body>
<div class="site">
  <div class="top-rule"></div>

  <header class="header">
    <div class="brand">
      <div class="brand-mark"></div>
      <div class="brand-name">Northgate<br>Cleaning Services</div>
    </div>
    <nav class="main-nav">
      <span>About Us</span><span>Our Services</span><span>Gallery</span><span>Contact</span>
    </nav>
    <span class="cta-button">Free Estimates</span>
  </header>

  <section class="hero" role="img" aria-label="Photo of a clean modern office with wooden floor, dining table and a glass-walled conference room">
    <div class="hero-disc">DO YOU<strong>NEED</strong>A<br>CLEANING</div>
  </section>

  <div class="info-bar">
    <span class="info-item">
      <svg width="12" height="12" viewBox="0 0 24 24"><path d="M6.6 10.8a15.1 15.1 0 0 0 6.6 6.6l2.2-2.2a1 1 0 0 1 1-.25 11.4 11.4 0 0 0 3.6.57 1 1 0 0 1 1 1V20a1 1 0 0 1-1 1A17 17 0 0 1 3 4a1 1 0 0 1 1-1h3.5a1 1 0 0 1 1 1c0 1.25.2 2.45.57 3.57a1 1 0 0 1-.25 1z"/></svg>
      +1 555 314 2760
    </span>
    <span class="info-item">
      <svg width="13" height="10" viewBox="0 0 26 20"><path d="M0 0h26v3L13 11 0 3z"/><path d="M0 6l13 8 13-8v14H0z"/></svg>
      info@northgateclean.com
    </span>
    <div class="social">
      <span class="social-dot blue" aria-label="Social link"></span>
      <span class="social-dot red" aria-label="Social link"></span>
      <span class="social-dot sky" aria-label="Social link"></span>
      <svg width="13" height="13" viewBox="0 0 24 24" fill="none" stroke="#6d6d6d" stroke-width="3"><circle cx="10" cy="10" r="6.5"/><path d="M15 15l6 6"/></svg>
    </div>
  </div>

  <section class="welcome">
    <h1>Welcome to <span>Northgate Cleaning Services</span></h1>
    <div class="dotted-rule"></div>
    <p>Sed ut perspiciatis unde omnis iste natus error sit voluptatem accusantium doloremque laudantium, totam rem aperiam, eaque ipsa quae ab illo inventore veritatis et quasi architecto beatae vitae dicta sunt explicabo.</p>
  </section>

  <div class="lower-band">
    <div class="outline-button"></div>
  </div>
</div>
</body>
</html>
```